Gym marketing agency needs an infographic

Looking for an infographic designed to fit 1920 X 1080 screen. Also, should be print ready as well.

Background: We help gym owners by offering a combination of web design (primary service) print promotional material that they can use and business coaching in the form of fitness business marketing strategies and campaigns. Our goal is to help gym owners get more clients.

We'll be hosting a webinar and I want to illustrate the following phases.

Phase One: Creating a valuable offer that attracts people who are interested in a solution that will help them get fit.

Phase Two: This is the promotion and marketing phase. This is where the gym will run various campaigns that promote their offer. We believe that there are only 3 ways to promote a gym and we call these the 3 gym marketing buckets. I would like to illustrate this. If it helps, the buckets are... relationship marketing, digital outreach, and print advertising.

Phase Three: Identifying opportunities. This is where people respond to our advertising efforts, take action, and become a fitness lead. We typically do this through a simple optin form on their gym website (which we will design)

There are now a few routes from there. We want to get a commitment. A commitment to actually come in to the gym. We do this with a 2 step process to try to get instant commitment. The first step is the previous optin form and this immediate next step is a booking calendar where they can schedule a time to come into the gym.

Another route is that they do not book an appointment on the spot. Since we have their contact info from the optin form, this is where we follow-up (phone, text and email) to get a commitment to come in. This is a delayed commitment.

So, the 2 options are either an instant commitment (ideal scenario) or a delayed commitment (not ideal but the emphasis is not on the follow up process)

Once they schedule a time to come in, we want to get them into the gym. This is where a secondary follow up system come in. This is basically a friendly reminder sequence to minimize no shows. Minimize no shows should be emphasized here.

Once they come in and take advantage of the offer, the main goal is to get them to convert into a paying gym client.

You can take a look at our logo and site colors at https://trellowaypress.com/

```html
<!DOCTYPE html>
<html lang="en">
<head>
<meta charset="UTF-8">
<title>Fitness Business Marketing Strategies and Campaigns</title>
<link rel="stylesheet" href="https://fonts.googleapis.com/css2?family=Oswald:wght@500;600;700&family=Roboto:wght@300;400;700&display=swap">
<style>
  :root {
    --blue: #35aedb;
    --dark: #373737;
    --white: #ffffff;
    --ink: #2f2f2f;
    --tag-fill: #4fbbe2;
  }
  * { box-sizing: border-box; margin: 0; padding: 0; }
  html, body { width: 1200px; height: 675px; overflow: hidden; background: var(--white); }
  .infographic { position: relative; width: 1200px; height: 675px; background: var(--white); font-family: 'Roboto', sans-serif; }
  .main-title {
    position: absolute; top: 22px; left: 0; width: 100%;
    text-align: center; font-family: 'Oswald', sans-serif; font-weight: 700;
    font-size: 38px; letter-spacing: 2px; color: var(--dark); line-height: 56px;
  }
  .phases { position: absolute; top: 87.5px; left: 0; width: 1200px; height: 519px; display: flex; }
  .phase { position: relative; width: 240px; height: 100%; }
  .phase--blue { background: var(--blue); color: var(--white); }
  .phase--dark { background: var(--dark); color: var(--white); }
  .phase--light { background: var(--white); color: var(--ink); }
  .phase--blue.phase--dark-text { color: var(--ink); }
  .pointer { position: absolute; top: 243px; right: -19px; width: 19px; height: 32px; z-index: 2; }
  .kettlebell { position: absolute; top: 25px; left: 95px; width: 50px; height: 72px; }
  .phase-title {
    position: absolute; top: 112px; left: 8px; right: 8px; height: 54px;
    display: flex; align-items: center; justify-content: center; text-align: center;
    font-family: 'Oswald', sans-serif; font-weight: 700; font-size: 20.5px;
    letter-spacing: 1px; line-height: 24.4px; text-transform: uppercase;
  }
  .phase-body {
    position: absolute; top: 180px; left: 31px; width: 178px;
    font-weight: 300; font-size: 13.6px; line-height: 19.4px; text-align: justify;
  }
  .commitment { position: absolute; left: 31px; width: 178px; }
  .commitment--instant { top: 180px; }
  .commitment--delayed { top: 336px; }
  .commitment h3 {
    font-family: 'Oswald', sans-serif; font-weight: 700; font-size: 15.5px;
    letter-spacing: 0.6px; line-height: 20px; text-transform: uppercase; white-space: nowrap;
  }
  .commitment p { font-weight: 300; font-size: 13.6px; line-height: 19.4px; text-align: justify; margin-top: 2px; }
  .artwork { position: absolute; }
  .artwork--offer { left: 94px; top: 400px; width: 50px; height: 94px; border-radius: 10px 10px 6px 6px; background: var(--tag-fill); border: 1.5px solid var(--white); transform: skewY(-22deg); }
  .artwork--buckets { left: 18px; top: 394px; width: 198px; height: 103px; border-radius: 8px; background: linear-gradient(135deg, #4a4a4a, #2c2c2c); border: 1px solid #5a5a5a; }
  .artwork--optin { left: 62px; top: 425px; width: 116px; height: 69px; border-radius: 8px; background: linear-gradient(135deg, #f3f3f3, #dcdcdc); border: 1px solid #bdbdbd; }
  .brand {
    position: absolute; top: 628px; left: 0; width: 100%;
    display: flex; align-items: center; justify-content: center; gap: 8px;
  }
  .brand-dot { width: 22px; height: 22px; border-radius: 50%; background: var(--blue); }
  .brand-name { font-family: 'Roboto', sans-serif; font-weight: 700; font-size: 22px; color: var(--dark); letter-spacing: 0.3px; }
</style>
</head>
<body>
<main class="infographic">
  <h1 class="main-title">FITNESS BUSINESS MARKETING STRATEGIES AND CAMPAIGNS</h1>

  <section class="phases">
    <article class="phase phase--blue">
      <svg class="kettlebell" viewBox="0 0 50 72" aria-hidden="true">
        <path d="M9 26 C2 14 8 2 25 2 C42 2 48 14 41 26 L34 26 C38 18 34 11 25 11 C16 11 12 18 16 26 Z" fill="var(--dark)"/>
        <circle cx="25" cy="46" r="25" fill="var(--dark)"/>
        <text x="25" y="58" text-anchor="middle" font-family="Oswald, sans-serif" font-weight="700" font-size="32" fill="var(--blue)">1</text>
      </svg>
      <h2 class="phase-title">Valuable Offer</h2>
      <p class="phase-body">Creating a valuable offer that attracts people who are interested in a solution that will help them get fit</p>
      <div class="artwork artwork--offer" role="img" aria-label="Price tag illustration marked 50% off"></div>
      <svg class="pointer" viewBox="0 0 19 32" preserveAspectRatio="none" aria-hidden="true"><path d="M0 0 L19 16 L0 32 Z" fill="var(--blue)"/></svg>
    </article>

    <article class="phase phase--dark">
      <svg class="kettlebell" viewBox="0 0 50 72" aria-hidden="true">
        <path d="M9 26 C2 14 8 2 25 2 C42 2 48 14 41 26 L34 26 C38 18 34 11 25 11 C16 11 12 18 16 26 Z" fill="var(--blue)"/>
        <circle cx="25" cy="46" r="25" fill="var(--blue)"/>
        <text x="25" y="58" text-anchor="middle" font-family="Oswald, sans-serif" font-weight="700" font-size="32" fill="var(--dark)">2</text>
      </svg>
      <h2 class="phase-title">Promotion and<br>Marketing Phase</h2>
      <p class="phase-body">The gym will run various campaigns that promote their offer. We believe that there are only 3 ways to promote a gym and we call these the 3 gym marketing buckets. The buckets are relationship marketing, digital outreach, and print advertising.</p>
      <div class="artwork artwork--buckets" role="img" aria-label="Line illustration of a handshake, a phone with app icons and a print ad flyer"></div>
      <svg class="pointer" viewBox="0 0 19 32" preserveAspectRatio="none" aria-hidden="true"><path d="M0 0 L19 16 L0 32 Z" fill="var(--dark)"/></svg>
    </article>

    <article class="phase phase--light">
      <svg class="kettlebell" viewBox="0 0 50 72" aria-hidden="true">
        <path d="M9 26 C2 14 8 2 25 2 C42 2 48 14 41 26 L34 26 C38 18 34 11 25 11 C16 11 12 18 16 26 Z" fill="var(--dark)"/>
        <circle cx="25" cy="46" r="25" fill="var(--dark)"/>
        <text x="25" y="58" text-anchor="middle" font-family="Oswald, sans-serif" font-weight="700" font-size="32" fill="var(--white)">3</text>
      </svg>
      <h2 class="phase-title">Identifying<br>Opportunities</h2>
      <p class="phase-body">People respond to our advertising efforts, take action, and become a fitness lead. We typically do this through a simple optin form on their gym website (which we will design)</p>
      <div class="artwork artwork--optin" role="img" aria-label="Line illustration of a tablet showing an optin form"></div>
      <svg class="pointer" viewBox="0 0 19 32" preserveAspectRatio="none" aria-hidden="true"><path d="M0 0 L19 16 L0 32 Z" fill="var(--white)"/></svg>
    </article>

    <article class="phase phase--blue phase--dark-text">
      <svg class="kettlebell" viewBox="0 0 50 72" aria-hidden="true">
        <path d="M9 26 C2 14 8 2 25 2 C42 2 48 14 41 26 L34 26 C38 18 34 11 25 11 C16 11 12 18 16 26 Z" fill="var(--dark)"/>
        <circle cx="25" cy="46" r="25" fill="var(--dark)"/>
        <text x="25" y="58" text-anchor="middle" font-family="Oswald, sans-serif" font-weight="700" font-size="32" fill="var(--blue)">4</text>
      </svg>
      <h2 class="phase-title">Get a Commitment</h2>
      <div class="commitment commitment--instant">
        <h3>1. Instant Commitment</h3>
        <p>The first step is the previous optin form and this immediate next step is a booking calendar where they can schedule a time to come into the gym.</p>
      </div>
      <div class="commitment commitment--delayed">
        <h3>2. Delayed Commitment</h3>
        <p>They do not book an appointment on the spot. But since we have their contact info from the optin form, this is where we follow-up (phone, text and email) to get a commitment to come in.</p>
      </div>
      <svg class="pointer" viewBox="0 0 19 32" preserveAspectRatio="none" aria-hidden="true"><path d="M0 0 L19 16 L0 32 Z" fill="var(--blue)"/></svg>
    </article>

    <article class="phase phase--dark">
      <svg class="kettlebell" viewBox="0 0 50 72" aria-hidden="true">
        <path d="M9 26 C2 14 8 2 25 2 C42 2 48 14 41 26 L34 26 C38 18 34 11 25 11 C16 11 12 18 16 26 Z" fill="var(--blue)"/>
        <circle cx="25" cy="46" r="25" fill="var(--blue)"/>
        <text x="25" y="58" text-anchor="middle" font-family="Oswald, sans-serif" font-weight="700" font-size="32" fill="var(--dark)">5</text>
      </svg>
      <h2 class="phase-title">Secondary<br>Follow Up System</h2>
      <p class="phase-body">Once they schedule a time to come in, we want to get them into the gym. This is where a secondary follow up system come in. This is basically a friendly reminder sequence to minimize no shows. Minimize no shows should be emphasized here. Once they come in and take advantage of the offer, the main goal is to get them to convert into a paying gym client.</p>
    </article>
  </section>

  <footer class="brand">
    <span class="brand-dot" aria-hidden="true"></span>
    <span class="brand-name">Trelloway Press</span>
  </footer>
</main>
</body>
</html>
```